flatrotate.co.uk landing page website design

Hi designers, I would like a custom designed landing page very similar to www.dwellingtrader.co.uk. It represents a happy place, sunny days and people swapping homes. I would like this done just like theres but our own design but a similar layout as theres.

I would like the 3 reasons to use us to be

Connect to thousands of other people in your area looking for a home swap

Our service is Completely free unlike most other exchange websites.

Find a exchange within 30 days!*

Thank you all,

Hi Everyone, I need the designs to represent london if possible like one of the designers has done for anyone else being in with a chance to win. Please check out the design by KR with the london look. I still like some of the others and they may win but i need to give this a try please.

Target Market(s)

Council house tenants

Coding

Coded - Design and coding required

Number of Pages Required

1 page

Requirements
Must have
• Custom designed landing page showing all the elements that www.dwellingtrader.co.uk use, The blue sky, and the land it shows with houses and people representing people swapping house. It can not be the same as them but can be similar concept with our own custom design and colour scheme ect.

please create 3 bubbles for speech from people. Please add the following quotes. "Its time we upsize"
"lets try and downsize and save money" "shall we move house?"
Would like 2 blocks of flats in a similar way dwelling trader.co.uk show the houses.
Nice to have

Should not have
• Same colour scheme as dwelling trader apart from the blue sky

```html
<!DOCTYPE html>
<html lang="en">
<head>
<meta charset="utf-8">
<title>flatrotate.co.uk – Your dream home is a moment away</title>
<link rel="stylesheet" href="https://fonts.googleapis.com/css2?family=Lato:wght@400;700&family=Nunito:wght@800;900&display=swap">
<style>
  :root {
    --sky: #c4e6f8;
    --green: #3cb54a;
    --green-soft: #4dbd5e;
    --red: #ff3a0a;
    --ink: #111111;
    --white: #ffffff;
    --muted: #a9a9a9;
    --footer: #000000;
    --footer-text: #9a9a9a;
    --road: #8a8585;
  }
  * { box-sizing: border-box; margin: 0; padding: 0; }
  html, body { width: 865px; height: 1200px; overflow: hidden; }
  body { font-family: "Lato", sans-serif; color: var(--ink); background: var(--white); }
  .page { position: relative; width: 865px; height: 1200px; }

  .hero { position: absolute; left: 0; top: 0; width: 865px; height: 842px; background: var(--sky); }

  .brand { position: absolute; left: 63px; top: 40px; display: flex; align-items: center; gap: 8px; }
  .brand-mark { width: 30px; height: 30px; background: var(--green); }
  .brand-name { font-family: "Lato", sans-serif; font-weight: 700; font-size: 24px; color: var(--ink); letter-spacing: -0.3px; }

  .account-nav { position: absolute; top: 42px; left: 631px; display: flex; gap: 5px; }
  .pill { display: flex; align-items: center; justify-content: center; width: 75px; height: 23px; border-radius: 12px; color: var(--white); font-size: 12px; text-decoration: none; }
  .pill--dark { background: var(--ink); }
  .pill--red { background: var(--red); }

  .intro { position: absolute; left: 165px; top: 183px; width: 229px; text-align: center; }
  .intro-title { font-family: "Nunito", sans-serif; font-weight: 900; font-size: 19px; letter-spacing: 0.2px; }
  .intro-sub { font-size: 19px; margin-top: 6px; }
  .role-btn { display: flex; align-items: center; justify-content: center; height: 32px; border-radius: 16px; font-family: Arial, sans-serif; font-size: 15px; text-decoration: none; }
  .role-btn--tenant { position: absolute; top: 68px; width: 229px; background: var(--white); color: var(--red); }
  .role-btn--landlord { position: absolute; top: 112px; width: 229px; background: var(--red); color: var(--white); border: 1px solid #c02a00; }

  .search-panel { position: absolute; left: 462px; top: 145px; width: 275px; height: 275px; background: var(--green); border-radius: 18px; box-shadow: 0 4px 8px rgba(0,0,0,0.18); font-family: Arial, sans-serif; }
  .field-label { position: absolute; left: 32px; color: var(--white); font-size: 11px; }
  .field { position: absolute; left: 24px; width: 229px; height: 31px; border-radius: 16px; background: var(--white); border: 1px solid #d8d8d8; color: var(--muted); font-size: 11px; padding-left: 13px; display: flex; align-items: center; }
  .field svg { position: absolute; right: 14px; top: 11px; }
  .search-btn { position: absolute; left: 101px; top: 228px; width: 75px; height: 23px; border-radius: 12px; background: var(--ink); color: var(--white); font-size: 12px; display: flex; align-items: center; justify-content: center; }

  .street-scene { position: absolute; left: 0; top: 481px; width: 865px; height: 361px;
    background: linear-gradient(180deg, #d9eef9 0%, #f3f8fb 22%, #e7c3a2 42%, #9fd26a 62%, #a79f9b 72%, var(--road) 100%);
    border-bottom-left-radius: 50% 18px; border-bottom-right-radius: 50% 18px; }
  .bubble { position: absolute; background: rgba(255,255,255,0.9); font-family: Arial, sans-serif; font-size: 12px; line-height: 15px; text-align: center; display: flex; align-items: center; justify-content: center; }
  .bubble--downsize { left: 362px; top: 543px; width: 110px; height: 68px; border-radius: 14px; color: var(--green); }
  .bubble--upsize { left: 525px; top: 599px; width: 100px; height: 116px; border-radius: 50%; color: var(--red); background: rgba(255,255,255,0.6); }
  .bubble--move { left: 220px; top: 657px; width: 120px; height: 80px; border-radius: 50%; color: var(--red); }

  .reasons-title { position: absolute; top: 876px; width: 865px; text-align: center; font-family: "Nunito", sans-serif; font-weight: 900; font-size: 19px; }
  .reason { position: absolute; top: 944px; width: 126px; text-align: center; }
  .reason-icon { width: 106px; height: 106px; margin: 0 auto; border-radius: 50%; background: var(--green-soft); box-shadow: 0 5px 5px rgba(0,0,0,0.12); display: flex; align-items: center; justify-content: center; }
  .reason-strong { margin-top: 15px; font-family: "Nunito", sans-serif; font-weight: 900; font-size: 12px; color: var(--green); }
  .reason-text { font-size: 12px; line-height: 15px; }

  .site-footer { position: absolute; left: 0; top: 1150px; width: 865px; height: 50px; background: var(--footer); color: var(--footer-text); font-size: 11px; }
  .site-footer a { position: absolute; top: 18px; color: var(--footer-text); text-decoration: none; }
  .copyright { position: absolute; top: 18px; right: 63px; }
</style>
</head>
<body>
<div class="page">
  <header class="hero">
    <div class="brand">
      <span class="brand-mark"></span>
      <span class="brand-name">flatrotate.co.uk</span>
    </div>
    <nav class="account-nav">
      <a class="pill pill--dark" href="#">Sign Up</a>
      <a class="pill pill--red" href="#">Login</a>
    </nav>

    <section class="intro">
      <h1 class="intro-title">YOUR DREAM</h1>
      <p class="intro-sub">Home is a moment away!</p>
      <a class="role-btn role-btn--tenant" href="#">Are You A Tenant?</a>
      <a class="role-btn role-btn--landlord" href="#">Are You A Landlord?</a>
    </section>

    <form class="search-panel">
      <span class="field-label" style="top:40px">Location</span>
      <div class="field" style="top:52px">Town or post code</div>
      <span class="field-label" style="top:95px">Bed Rooms</span>
      <div class="field" style="top:112px">Any
        <svg width="14" height="8" viewBox="0 0 14 8"><path d="M1 1l6 6 6-6" fill="none" stroke="#999" stroke-width="1.4"/></svg>
      </div>
      <span class="field-label" style="top:155px">Max. Rent (£ Per Month)</span>
      <div class="field" style="top:172px">Any
        <svg width="14" height="8" viewBox="0 0 14 8"><path d="M1 1l6 6 6-6" fill="none" stroke="#999" stroke-width="1.4"/></svg>
      </div>
      <div class="search-btn">Search</div>
    </form>

    <div class="street-scene" role="img" aria-label="Illustrated sunny street with houses, trees and people walking, cycling and talking about swapping homes"></div>
    <p class="bubble bubble--downsize">"lets try and<br>downsize and<br>save money"</p>
    <p class="bubble bubble--upsize">"Its time<br>we upsize"</p>
    <p class="bubble bubble--move">"shall we move<br>house?"</p>
  </header>

  <h2 class="reasons-title">Why Choose Us?</h2>

  <div class="reason" style="left:179px">
    <div class="reason-icon">
      <svg width="56" height="56" viewBox="0 0 56 56" fill="none" stroke="#fff" stroke-width="2"><path d="M4 26L28 4l24 22"/><path d="M10 22v28h36V22"/><rect x="20" y="28" width="16" height="14"/><path d="M20 34h16"/></svg>
    </div>
    <p class="reason-strong">Best</p>
    <p class="reason-text">Services</p>
  </div>
  <div class="reason" style="left:305px">
    <div class="reason-icon">
      <svg width="58" height="50" viewBox="0 0 58 50" fill="none" stroke="#fff" stroke-width="1.8"><path d="M12 4l2 4h4l-3 3 1 4-4-2-4 2 1-4-3-3h4z"/><path d="M29 2l2 4h4l-3 3 1 4-4-2-4 2 1-4-3-3h4z"/><path d="M46 4l2 4h4l-3 3 1 4-4-2-4 2 1-4-3-3h4z"/><circle cx="12" cy="26" r="4"/><circle cx="29" cy="24" r="4"/><circle cx="46" cy="26" r="4"/><path d="M2 46v-8a6 6 0 0 1 20 0v8M19 46v-10a10 8 0 0 1 20 0v10M36 46v-8a6 6 0 0 1 20 0v8M2 46h54"/></svg>
    </div>
    <p class="reason-strong">200 +</p>
    <p class="reason-text">Satisfied Clients</p>
  </div>
  <div class="reason" style="left:431px">
    <div class="reason-icon">
      <svg width="56" height="56" viewBox="0 0 56 56" fill="none" stroke="#fff" stroke-width="3" stroke-linejoin="round"><path d="M6 26L28 4l22 22"/><path d="M12 20v30h32V20"/><circle cx="28" cy="31" r="6"/><path d="M24 40l2-4"/></svg>
    </div>
    <p class="reason-strong">5 +</p>
    <p class="reason-text">Years of<br>experience</p>
  </div>
  <div class="reason" style="left:557px">
    <div class="reason-icon">
      <svg width="60" height="50" viewBox="0 0 60 50" fill="none" stroke="#fff" stroke-width="1.8"><path d="M2 48h56"/><path d="M10 48V10l16-6v44"/><path d="M30 48V8l16-6v46"/><path d="M14 16h8M14 24h8M14 32h8M14 40h8M34 14h8M34 22h8M34 30h8M34 38h8"/></svg>
    </div>
    <p class="reason-strong">Quality</p>
    <p class="reason-text">of Houses</p>
  </div>

  <footer class="site-footer">
    <a href="#" style="left:63px">Terms &amp; Condition</a>
    <a href="#" style="left:187px">Privacy Policy</a>
    <span class="copyright">© Copyright 2020, flatrotate.co.uk All Rights Reserved.</span>
  </footer>
</div>
</body>
</html>
```